Pricing Poster selling novelty toys and snacks at a Halloween event

I need a poster made for our Halloween event. It would incorporate the items offered and pricing for each.

selling novelty toys and snacks

The Poster needs to say :
PRICE LIST
Bracelets $8 for 1, 4 for $20
Toys $15 for 1, $20 for 2 |
Popcorn $5
Cotton Candy $5
CIDER $4

```html
<!DOCTYPE html>
<html lang="en">
<head>
<meta charset="utf-8">
<title>Halloween Price List Poster</title>
<link href="https://fonts.googleapis.com/css2?family=Creepster&family=Bangers&family=Bowlby+One&display=swap" rel="stylesheet">
<style>
  :root {
    --stage: #b4b4b4;
    --night: #000000;
    --purple: #4d1e52;
    --orange: #e8901c;
    --orange-deep: #e07f12;
    --white: #ffffff;
    --pumpkin: #f0a020;
    --hat: #5a2a6a;
    --icon-grey: #e6e6e6;
  }
  * { box-sizing: border-box; margin: 0; padding: 0; }
  html, body { width: 1200px; height: 900px; overflow: hidden; }
  body {
    background: var(--stage);
    position: relative;
    font-family: "Bangers", "Impact", sans-serif;
  }
  .poster {
    position: absolute;
    left: 270px; top: 20px;
    width: 660px; height: 860px;
    background: var(--night);
    overflow: hidden;
    color: var(--white);
  }
  .poster > * { position: absolute; }

  .art { border-radius: 50%; }
  .pumpkin {
    width: 88px; height: 74px;
    background: radial-gradient(circle at 45% 40%, #ffd24a, var(--pumpkin) 55%, #d8600c);
  }
  .pumpkin--left { left: 36px; top: 34px; }
  .pumpkin--right { left: 548px; top: 108px; }

  .bat { background: var(--white); border-radius: 50% 50% 40% 40%; }
  .bat--top { left: 300px; top: 86px; width: 76px; height: 20px; }
  .bat--ribbon-left { left: 62px; top: 444px; width: 64px; height: 24px; background: var(--night); }
  .bat--ribbon-right { left: 488px; top: 474px; width: 72px; height: 26px; background: var(--night); }

  .headline-blob { left: 20px; top: 96px; width: 620px; height: 320px; }

  .headline { left: 0; width: 660px; text-align: center; line-height: 1; }
  .headline--selling {
    top: 132px;
    font-family: "Creepster", cursive;
    color: var(--orange);
    font-size: 68px;
    letter-spacing: 2px;
    transform: rotate(3deg);
  }
  .headline--toys {
    top: 214px; left: -20px;
    font-size: 64px;
    letter-spacing: 1px;
    transform: rotate(4deg);
  }
  .headline--snacks {
    top: 300px; left: 80px;
    font-size: 64px;
    letter-spacing: 1px;
    transform: rotate(5deg);
  }
  .moon {
    left: 520px; top: 152px;
    width: 26px; height: 26px;
    border-radius: 50%;
    box-shadow: -5px 3px 0 0 var(--white);
  }
  .icon-candy-floss { width: 50px; height: 50px; background: var(--icon-grey); }
  .headline-candy { left: 540px; top: 222px; }
  .icon-bracelet { width: 100px; height: 36px; border-radius: 40%; background: linear-gradient(90deg, #6b4a72, #d9d9d9); }
  .headline-bracelet { left: 160px; top: 322px; }

  .ribbon { left: 20px; top: 420px; width: 620px; height: 100px; }
  .ribbon-label {
    left: 0; width: 660px; top: 450px; text-align: center;
    color: var(--night); font-size: 40px; line-height: 1;
    transform: rotate(4deg);
  }

  .label { font-family: "Creepster", cursive; color: var(--orange); line-height: 0.95; }
  .detail { font-size: 22px; line-height: 1.15; letter-spacing: 1px; }
  .price { font-family: "Bowlby One", sans-serif; color: var(--white); line-height: 1; }

  .item-bracelets-title { left: 34px; top: 522px; font-size: 50px; }
  .item-bracelets-icon { left: 28px; top: 590px; width: 90px; height: 34px; }
  .item-bracelets-one { left: 128px; top: 582px; }
  .item-bracelets-four { left: 222px; top: 582px; }
  .divider-small { left: 208px; top: 584px; width: 2px; height: 52px; background: var(--white); }

  .divider-v1 { left: 318px; top: 530px; width: 3px; height: 120px; background: var(--white); transform: rotate(8deg); }
  .item-toys-title { left: 340px; top: 534px; font-size: 54px; }
  .item-toys-icon { left: 440px; top: 548px; width: 46px; height: 42px; background: linear-gradient(#f2f2f2, var(--orange)); }
  .item-toys-detail { left: 340px; top: 596px; font-size: 20px; }

  .divider-v2 { left: 494px; top: 534px; width: 3px; height: 116px; background: var(--white); transform: rotate(8deg); }
  .item-popcorn-title { left: 508px; top: 544px; font-size: 40px; }
  .item-popcorn-icon { left: 602px; top: 542px; width: 36px; height: 42px; border-radius: 4px; background: linear-gradient(#f5f5f5, #cfcfcf); }
  .item-popcorn-price { left: 590px; top: 606px; font-size: 38px; }

  .divider-h { left: 30px; top: 664px; width: 600px; height: 3px; background: var(--white); transform: rotate(3deg); }

  .item-candy-icon { left: 28px; top: 690px; width: 44px; height: 50px; }
  .item-candy-title { left: 80px; top: 684px; font-size: 36px; transform: rotate(4deg); }
  .item-candy-price { left: 198px; top: 688px; font-size: 56px; }

  .divider-v3 { left: 302px; top: 688px; width: 3px; height: 64px; background: var(--white); transform: rotate(8deg); }
  .item-cider-title { left: 326px; top: 682px; font-size: 70px; }
  .item-cider-icon { left: 512px; top: 716px; width: 14px; height: 32px; border-radius: 4px 4px 2px 2px; background: var(--white); }
  .item-cider-price { left: 534px; top: 690px; font-size: 56px; }

  .drip { left: 0; top: 770px; width: 660px; height: 90px; }
  .hat { left: 250px; top: 764px; width: 84px; height: 40px; border-radius: 50% 50% 20% 20%; background: linear-gradient(var(--hat), #2e1036); }
</style>
</head>
<body>
<main class="poster">
  <div class="art pumpkin pumpkin--left" role="img" aria-label="Jack-o'-lantern pumpkin illustration"></div>
  <div class="art pumpkin pumpkin--right" role="img" aria-label="Jack-o'-lantern pumpkin illustration"></div>

  <svg class="headline-blob" viewBox="0 0 620 340" preserveAspectRatio="none" aria-hidden="true">
    <path d="M150 40 C200 0 300 0 360 20 C420 0 520 10 540 70 C600 80 610 150 590 190 C620 240 600 300 560 310 C500 340 300 330 160 320 C110 320 90 280 110 250 C30 240 10 190 50 150 C20 100 80 50 150 40 Z" fill="var(--orange)" transform="translate(0 8)"/>
    <path d="M150 40 C200 0 300 0 360 20 C420 0 520 10 540 70 C600 80 610 150 590 190 C620 240 600 300 560 310 C500 340 300 330 160 320 C110 320 90 280 110 250 C30 240 10 190 50 150 C20 100 80 50 150 40 Z" fill="var(--purple)"/>
  </svg>
  <div class="bat bat--top" role="img" aria-label="Flying bat illustration"></div>

  <div class="headline headline--selling">SELLING</div>
  <div class="moon" aria-hidden="true"></div>
  <div class="headline headline--toys">NOVELTY TOYS</div>
  <div class="art icon-candy-floss headline-candy" role="img" aria-label="Cotton candy illustration"></div>
  <div class="icon-bracelet headline-bracelet" role="img" aria-label="Charm bracelet illustration"></div>
  <div class="headline headline--snacks">&amp; SNACKS</div>

  <svg class="ribbon" viewBox="0 0 620 100" aria-hidden="true">
    <path d="M0 8 L610 50 L596 74 L614 92 L14 52 L26 32 Z" fill="var(--white)"/>
  </svg>
  <div class="bat bat--ribbon-left" role="img" aria-label="Bat silhouette"></div>
  <div class="ribbon-label">PRICE LIST</div>
  <div class="bat bat--ribbon-right" role="img" aria-label="Bat silhouette"></div>

  <div class="label item-bracelets-title">BRACELETS</div>
  <div class="icon-bracelet item-bracelets-icon" role="img" aria-label="Charm bracelet illustration"></div>
  <div class="detail item-bracelets-one">$8<br>FOR 1.</div>
  <div class="divider-small" aria-hidden="true"></div>
  <div class="detail item-bracelets-four">4 FOR<br>$20</div>

  <div class="divider-v1" aria-hidden="true"></div>
  <div class="label item-toys-title">TOYS</div>
  <div class="art item-toys-icon" role="img" aria-label="Teddy bear and ball toy illustration"></div>
  <div class="detail item-toys-detail">$15 FOR 1.<br>$20 FOR 2</div>

  <div class="divider-v2" aria-hidden="true"></div>
  <div class="label item-popcorn-title">POP<br>CORN</div>
  <div class="item-popcorn-icon" role="img" aria-label="Popcorn bucket illustration"></div>
  <div class="price item-popcorn-price">$5</div>

  <div class="divider-h" aria-hidden="true"></div>

  <div class="art icon-candy-floss item-candy-icon" role="img" aria-label="Cotton candy illustration"></div>
  <div class="label item-candy-title">COTTON<br>CANDY</div>
  <div class="price item-candy-price">$5</div>

  <div class="divider-v3" aria-hidden="true"></div>
  <div class="label item-cider-title">CIDER</div>
  <div class="item-cider-icon" role="img" aria-label="Cider bottle"></div>
  <div class="price item-cider-price">$4</div>

  <svg class="drip" viewBox="0 0 660 90" preserveAspectRatio="none" aria-hidden="true">
    <path d="M0 4 C40 0 80 10 110 4 C140 0 150 20 170 40 C190 60 210 24 230 12 C260 0 270 40 290 64 C310 84 330 60 350 60 C380 60 400 40 430 46 C460 52 450 80 480 80 C520 80 530 40 560 34 C600 26 620 60 660 54 L660 90 L0 90 Z" fill="var(--orange-deep)"/>
  </svg>
  <div class="hat" role="img" aria-label="Witch hat illustration"></div>
</main>
</body>
</html>
```